Mobile App UI for Telecommunications/Hosting Company

We are about to convert our existing self-service Customer Portal into a mobile phone application and need an elegant and professional UI/UX design. Our company provides telecommunication (voice/mobile/data) and hosting services to medium-sized business. The primary purpose of the application is to view trouble tickets, alerts, orders, and performance charts. This application is available to customers only - not the general public.

Please provide a UI design suitable for display on iPhone/Android devices. The attached document includes a proposed screen flow. You are free to design your own screens to display the same information elegantly.
Updates

Please note that the design should be based on the wireframes in the Word document, not the screenshots.  The screenshots are just to show our existing web portal look & feel.

Also, just a few screens are required for initial submission (3 would be great).

Thanks,
Dermot.

Target Market(s)

IT Managers away from their desk and using a mobile phone application.
Adult males from technical background aged 30-50.
Customers of Brindlewood Networks have access to this application (not the general public). This is a self-service portal for customers only.

Industry/Entity Type

Business

Colors
0592cd
33a6d7
85cae6
cadf82
fde08a

Requirements
Must have
• Please look at the screenshots from our current Customer Portal site (part of the project brief). The mobile app does not have to look the same, but should follow a similar style.

Please check out our company web site at www.brindlewoodnetworks.example (this site is not the customer portal and has a different look at feel) to understand what Brindlewood Networks does.
Nice to have
• Sharing capabilities via email/SMS.
A nice background image to make it stand out
The colours selected below are a guide only as they are similar to the corporate colours
- The priority is something that works on a phone - a design extendable to tablets is a nice to have as our existing web site looks OK on a tablet..

```html
<!DOCTYPE html>
<html lang="en">
<head>
<meta charset="utf-8">
<title>Brindlewood Networks – Alerts</title>
<link rel="stylesheet" href="https://fonts.googleapis.com/css2?family=Roboto:wght@300;400&display=swap">
<style>
  :root{
    --rail:#2f2f2f;
    --rail-line:#454545;
    --rail-active:#bdbdbd;
    --header:#4a4847;
    --white:#ffffff;
    --date:#f3d36a;
    --sunday:#e8415f;
    --muted:#d8d8d8;
    --divider:rgba(255,255,255,0.22);
  }
  *{margin:0;padding:0;box-sizing:border-box}
  html,body{width:676px;height:1200px;overflow:hidden;background:#fff}
  body{font-family:"Roboto",Arial,sans-serif;color:var(--white)}
  .app{position:relative;width:676px;height:1200px;overflow:hidden}
  .backdrop{position:absolute;inset:0;
    background:
      radial-gradient(ellipse 260px 360px at 560px 640px,rgba(40,40,40,.55),transparent 70%),
      radial-gradient(ellipse 220px 300px at 300px 900px,rgba(60,60,60,.45),transparent 70%),
      radial-gradient(ellipse 300px 260px at 420px 260px,rgba(170,165,160,.6),transparent 70%),
      linear-gradient(180deg,#8f8b88 0%,#77726f 35%,#6a6866 60%,#8a8885 100%)}
  .topbar{position:absolute;left:0;top:0;width:676px;height:101px;background:var(--header)}
  .brand{position:absolute;left:146px;top:31px;font-size:34px;font-weight:400;color:var(--white);letter-spacing:.5px;line-height:1.1}
  .profile{position:absolute;right:20px;top:22px;width:56px;height:56px}
  .rail{position:absolute;left:0;top:0;width:120px;height:1200px;background:var(--rail)}
  .rail-item{position:absolute;left:0;width:120px;height:125px;border-bottom:2px solid var(--rail-line);display:flex;align-items:center;justify-content:center}
  .rail-item.menu{top:0;height:101px;background:#3b3b3b;border-bottom:3px solid #5a5a5a}
  .rail-item.active{background:var(--rail-active)}
  .rail-item svg{width:52px;height:52px}
  .summary{position:absolute;left:148px;top:190px}
  .summary h1{font-size:58px;font-weight:400;letter-spacing:2px;line-height:1}
  .summary .day{font-size:26px;margin-top:8px;letter-spacing:1px}
  .count{position:absolute;left:418px;top:162px;font-size:140px;font-weight:300;line-height:1}
  .alerts{position:absolute;left:120px;top:363px;width:556px;list-style:none}
  .alert{position:relative;height:126px;border-bottom:2px solid var(--divider);display:flex;align-items:center}
  .alert .date{position:absolute;left:32px;font-size:31px}
  .alert .date .num{color:var(--date)}
  .alert .level{position:absolute;left:383px;font-size:37px;font-weight:300;color:var(--muted)}
  .alert.weekend .dow,.alert.weekend .level{color:var(--sunday)}
  .alert:last-child{border-bottom:none}
  .column-rule{position:absolute;left:478px;top:363px;width:2px;height:837px;background:var(--divider)}
</style>
</head>
<body>
<div class="app">
  <div class="backdrop" role="img" aria-label="Blurred office background photograph in soft greys"></div>

  <header class="topbar">
    <div class="brand">Brindlewood Networks</div>
    <svg class="profile" viewBox="0 0 56 56" fill="none" stroke="#fff" stroke-width="3"><circle cx="28" cy="20" r="11"/><path d="M8 52c2-12 10-18 20-18s18 6 20 18z"/></svg>
  </header>

  <nav class="rail">
    <div class="rail-item menu"><svg viewBox="0 0 52 52" stroke="#fff" stroke-width="5"><path d="M4 14h44M4 26h44M4 38h44"/></svg></div>
    <div class="rail-item" style="top:101px"><svg viewBox="0 0 52 52" fill="none" stroke="#fff" stroke-width="3"><rect x="4" y="10" width="44" height="32" rx="6"/><path d="M6 14l20 16 20-16"/></svg></div>
    <div class="rail-item" style="top:226px"><svg viewBox="0 0 52 52" fill="none" stroke="#fff" stroke-width="3" stroke-linejoin="round"><path d="M46 6L6 24l16 6 6 16z"/><path d="M46 6L22 30"/></svg></div>
    <div class="rail-item active" style="top:351px"><svg viewBox="0 0 52 52" fill="none" stroke="#fff" stroke-width="3"><rect x="6" y="10" width="40" height="36" rx="4"/><path d="M6 18h40M16 5v9M36 5v9"/><path d="M16 26h4M26 26h4M36 26h2M16 34h4M26 34h4M36 34h2" stroke-width="4"/></svg></div>
    <div class="rail-item" style="top:476px"><svg viewBox="0 0 52 52" fill="none" stroke="#fff" stroke-width="3" stroke-linejoin="round"><path d="M4 36l12-12 10 8 12-14 10 10"/></svg></div>
    <div class="rail-item" style="top:601px"><svg viewBox="0 0 52 52" fill="none" stroke="#fff" stroke-width="3"><circle cx="26" cy="26" r="20"/><path d="M26 16v20M16 26h20"/></svg></div>
    <div class="rail-item" style="top:726px"><svg viewBox="0 0 52 52" fill="none" stroke="#fff" stroke-width="3"><path d="M3 26c6-10 14-15 23-15s17 5 23 15c-6 10-14 15-23 15S9 36 3 26z"/><circle cx="26" cy="26" r="7"/></svg></div>
    <div class="rail-item" style="top:851px"><svg viewBox="0 0 52 52" fill="none" stroke="#fff" stroke-width="3"><circle cx="26" cy="26" r="7"/><path d="M22 4h8l1 6 5 2 5-4 6 6-4 5 2 5 6 1v8l-6 1-2 5 4 5-6 6-5-4-5 2-1 6h-8l-1-6-5-2-5 4-6-6 4-5-2-5-6-1v-8l6-1 2-5-4-5 6-6 5 4 5-2z" stroke-linejoin="round"/></svg></div>
  </nav>

  <section class="summary">
    <h1>ALERTS</h1>
    <p class="day">FRI 29/06</p>
  </section>
  <div class="count">24</div>

  <div class="column-rule"></div>
  <ul class="alerts">
    <li class="alert"><span class="date"><span class="dow">SAT</span> <span class="num">29/06</span></span><span class="level">warning</span></li>
    <li class="alert weekend"><span class="date"><span class="dow">SUN</span> <span class="num">30/06</span></span><span class="level">warning</span></li>
    <li class="alert"><span class="date"><span class="dow">MON</span> <span class="num">01/07</span></span><span class="level">warning</span></li>
    <li class="alert"><span class="date"><span class="dow">TUE</span> <span class="num">02/07</span></span><span class="level">warning</span></li>
    <li class="alert"><span class="date"><span class="dow">WED</span> <span class="num">03/07</span></span><span class="level">warning</span></li>
    <li class="alert"><span class="date"><span class="dow">THU</span> <span class="num">04/07</span></span><span class="level">warning</span></li>
  </ul>
</div>
</body>
</html>
```